Beauty Salon
I would like to see designs using sky blue and a soft orange. Mainly I would like my name ( Glow N' Wave Salon ) used as the design

Industry/Entity Type

Business

Contact Information for Business Card

Glow N'Wave Salon
418 E Maple Dr #14
Willow Crest, Ca 90417
626 555-0172

```html
<!DOCTYPE html>
<html lang="en">
<head>
<meta charset="utf-8">
<title>Glow N' Wave Salon – Business Card</title>
<link href="https://fonts.googleapis.com/css2?family=Arimo:wght@400;700&display=swap" rel="stylesheet">
<style>
  :root {
    --sky: #9dd3ec;
    --sage: #c2c7b0;
    --sand: #d3bd96;
    --apricot: #e8b170;
    --ink: #2b2b2b;
    --icon-cut: #d2c6a6;
  }
  * { margin: 0; padding: 0; box-sizing: border-box; }
  html, body { width: 1200px; height: 704px; overflow: hidden; }
  body { font-family: "Arimo", Arial, sans-serif; color: var(--ink); }
  .card {
    position: relative;
    width: 1200px;
    height: 704px;
    background: linear-gradient(150deg, var(--sky) 0%, var(--sage) 38%, var(--sand) 68%, var(--apricot) 100%);
  }
  .brand-name {
    position: absolute;
    top: 150px;
    left: 0;
    width: 100%;
    text-align: center;
    font-size: 122px;
    font-weight: 400;
    letter-spacing: 3px;
    line-height: 130px;
    color: var(--ink);
  }
  .rule-heading {
    position: absolute;
    left: 177px;
    width: 847px;
    display: flex;
    align-items: center;
    gap: 14px;
    font-weight: 700;
    color: var(--ink);
  }
  .rule-heading::before,
  .rule-heading::after {
    content: "";
    flex: 1;
    height: 2px;
    background: var(--ink);
  }
  .tagline { top: 300px; font-size: 30px; letter-spacing: 1px; }
  .owner-name { top: 463px; font-size: 31px; letter-spacing: 0.5px; }
  .contact-line {
    position: absolute;
    top: 509px;
    left: 0;
    width: 100%;
    display: flex;
    justify-content: center;
    align-items: center;
    gap: 8px;
    font-size: 28.5px;
    font-weight: 400;
  }
  .contact-line svg { width: 29px; height: 29px; fill: var(--ink); }
  .contact-line .phone-icon { margin-left: 8px; }
</style>
</head>
<body>
  <main class="card">
    <h1 class="brand-name">Glow N' Wave</h1>
    <p class="rule-heading tagline">SALON</p>
    <p class="rule-heading owner-name">ROSALYN</p>
    <p class="contact-line">
      <svg class="pin-icon" viewBox="0 0 28 28" aria-hidden="true">
        <circle cx="14" cy="14" r="13"/>
        <path d="M14 6a5.5 5.5 0 0 0-5.5 5.5C8.5 15.5 14 22 14 22s5.5-6.5 5.5-10.5A5.5 5.5 0 0 0 14 6zm0 7.6a2.1 2.1 0 1 1 0-4.2 2.1 2.1 0 0 1 0 4.2z" fill="var(--icon-cut)"/>
      </svg>
      <span class="address">418 E Maple Dr #14,Willow Crest, Ca 90417</span>
      <svg class="phone-icon" viewBox="0 0 28 28" aria-hidden="true">
        <circle cx="14" cy="14" r="13"/>
        <rect x="9.5" y="6" width="9" height="16" rx="1.8" fill="var(--icon-cut)"/>
        <rect x="11" y="8" width="6" height="11" fill="var(--ink)"/>
      </svg>
      <span class="phone">626 555-0172</span>
    </p>
  </main>
</body>
</html>
```